Verpackungen für Duschbrausen
Zielgruppe
Wir verkaufen verschiedene Produkte über E-Commerce Plattformen. Zielgruppe sind in diesem Fall alle die eine neue Duschbrause benötigen.
Aufgabenstellung
Liebe Grafikerinnen und Grafiker,
wir werden eine neue Produktlinie von Duschbrausen auf den Markt bringen und benötigen dafür eine frische, ansprechende Umverpackung. Eure Kreativität und Expertise sind gefragt, um eine Verpackung zu gestalten, die sowohl für verschiedene Duschbrausenmodelle geeignet ist als auch neutral und ansprechend wirkt.
Unser Ziel ist es, eine Verpackung zu kreieren, die sich von anderen abhebt, aber dennoch einen gewissen Neutralitätsgrad beibehält. Die Verpackung sollte modern, professionell und ansprechend gestaltet sein, um die Aufmerksamkeit der Kunden zu gewinnen.
Im Anhang findet ihr Beispiele von anderen Firmen (Zip Datei Verpackung Mitbewerber), wie sie ihre Duschbrausen verpacken. Diese dienen lediglich zur Inspiration und sollen euch einen Einblick in den aktuellen Markt geben. Wir ermutigen euch jedoch dazu, eure eigenen kreativen Ideen einzubringen und eine einzigartige Umverpackung zu entwerfen.
Bitte beachtet bei euren Entwürfen folgende Punkte:
Neutralität: Die Verpackung sollte für verschiedene Duschbrausenmodelle geeignet sein.
Modernität: Ein zeitgemäßes Design
Ansprechendes Layout: Klare Strukturen und gut lesbare Informationen.
Wir sind sehr gespannt auf eure Vorschläge :-)
Bei Fragen oder Unklarheiten stehe ich euch gerne zur Verfügung. Vielen Dank im Voraus für eure kreative Arbeit!
Mit freundlichen Grüßen,
Bertold

```html
<!DOCTYPE html>
<html lang="de">
<head>
<meta charset="utf-8">
<title>Duschkopf Faltschachtel – Stanzbogen</title>
<link rel="stylesheet" href="https://fonts.googleapis.com/css2?family=Space+Grotesk:wght@300;400;500;700&display=swap">
<style>
  :root {
    --paper: #f5f5f5;
    --sky: #a6cff2;
    --sky-light: #b9daf5;
    --mist: #e6ebef;
    --ink: #111418;
    --cut: #2a2d31;
    --chrome-a: #dfe3e7;
    --chrome-b: #9aa3ab;
  }
  html, body { margin: 0; padding: 0; overflow: hidden; }
  body { width: 1200px; height: 1200px; background: var(--paper); }
  .dieline { display: block; width: 1200px; height: 1200px; font-family: "Space Grotesk", sans-serif; }
  .cut { fill: none; stroke: var(--cut); stroke-width: 1; }
  .fill-sky { fill: var(--sky); }
  .fill-mist { fill: var(--mist); }
  .fill-paper { fill: var(--paper); }
  .headline { fill: var(--ink); font-weight: 300; }
  .claim { fill: var(--ink); font-size: 17px; letter-spacing: 2px; font-weight: 400; }
  .size-note { fill: var(--ink); font-size: 13px; letter-spacing: 1px; }
  .copy-title { fill: var(--ink); font-size: 13px; font-weight: 700; letter-spacing: 1px; }
  .copy-body { fill: var(--ink); font-size: 12.5px; letter-spacing: 0.6px; }
  .mode-label { fill: var(--ink); font-size: 16px; letter-spacing: 2px; text-anchor: end; }
  .badge-text { fill: var(--ink); font-size: 7.5px; font-weight: 700; letter-spacing: 0.3px; }
</style>
</head>
<body>
<svg class="dieline" viewBox="0 0 1200 1200" xmlns="http://www.w3.org/2000/svg">
  <defs>
    <linearGradient id="chrome" x1="0" y1="0" x2="1" y2="1">
      <stop offset="0" stop-color="var(--chrome-a)"/>
      <stop offset="1" stop-color="var(--chrome-b)"/>
    </linearGradient>
    <radialGradient id="spray" cx="0.5" cy="0.4" r="0.6">
      <stop offset="0" stop-color="#c9cdd1"/>
      <stop offset="1" stop-color="#1e2124"/>
    </radialGradient>
    <path id="badge-arc" d="M672,389 A40,40 0 1 1 743,372"/>
  </defs>

  <!-- Back panel artwork -->
  <g class="back-panel">
    <rect class="fill-sky" x="106" y="62" width="222" height="308"/>
    <rect class="fill-mist" x="328" y="62" width="134" height="308"/>
    <path class="fill-paper" d="M106,370 C180,350 260,355 328,372 C380,382 430,372 462,365 L462,730 C420,722 380,730 328,722 C260,706 180,708 106,722 Z"/>
    <path class="fill-sky" d="M106,722 C180,708 260,706 328,722 L328,1183 L195,1183 L195,1140 L106,1056 Z"/>
    <path class="fill-mist" d="M328,722 C380,730 420,722 462,730 L462,1056 L372,1140 L372,1183 L328,1183 Z"/>

    <circle cx="180" cy="455" r="6" fill="#222"/>
    <text class="copy-title" x="198" y="460">DAS VOLLE PROGRAMM.</text>
    <text class="copy-body">
      <tspan x="172" y="477">Unsere  multifunktionale  Brause</tspan>
      <tspan x="172" y="495">bietet dir fünf verschiedene Ein-</tspan>
      <tspan x="172" y="513">stellungen – ganz wie im Urlaub.</tspan>
    </text>

    <circle cx="180" cy="591" r="6" fill="#1d3a78"/>
    <text class="copy-title" x="198" y="596">THE WHOLE NINE YARDS.</text>
    <text class="copy-body">
      <tspan x="172" y="613">Our multifunctional shower head</tspan>
      <tspan x="172" y="631">offers you five different settings</tspan>
      <tspan x="172" y="649">– just like on holiday.</tspan>
    </text>

    <g class="spray-modes">
      <text class="mode-label" x="308" y="785">RAINFALL.</text>
      <circle cx="371" cy="779" r="22" fill="url(#spray)" role="img" aria-label="Strahlart Rainfall"/>
      <text class="mode-label" x="308" y="841">WATERFALL MIST.</text>
      <circle cx="371" cy="835" r="22" fill="url(#spray)" role="img" aria-label="Strahlart Waterfall Mist"/>
      <text class="mode-label" x="308" y="897">MASSAGE.</text>
      <circle cx="371" cy="891" r="22" fill="url(#spray)" role="img" aria-label="Strahlart Massage"/>
      <text class="mode-label"><tspan x="308" y="941">RAINFALL +</tspan><tspan x="308" y="963">MASSAGE</tspan></text>
      <circle cx="371" cy="946" r="22" fill="url(#spray)" role="img" aria-label="Strahlart Rainfall und Massage"/>
      <text class="mode-label"><tspan x="308" y="1001">RAINFALL +</tspan><tspan x="308" y="1023">WATERFALL MIST.</tspan></text>
      <circle cx="371" cy="1007" r="22" fill="url(#spray)" role="img" aria-label="Strahlart Rainfall und Waterfall Mist"/>
    </g>
  </g>

  <!-- Side and front panel artwork -->
  <g class="front-panel">
    <path class="fill-mist" d="M610,270 L625,270 L625,205 C670,212 720,210 760,205 L760,1140 L715,1140 L715,1183 L625,1183 L625,1056 L570,1056 C585,900 600,700 597,520 C594,400 600,320 610,270 Z"/>
    <path class="fill-sky" d="M760,205 C820,210 900,212 982,207 L982,270 L1015,270 C1030,340 1020,420 1025,520 C1030,650 1020,800 1030,930 C1033,990 1030,1030 1030,1056 L982,1056 L982,1183 L892,1183 L892,1140 L760,1140 Z"/>

    <text class="size-note" x="766" y="292">⌀ 115 MM</text>

    <path fill="url(#chrome)" role="img" aria-label="Produktfoto Handbrause in Chrom mit runder Strahlscheibe"
      d="M640,520 C640,445 705,400 790,390 C880,385 905,450 900,540 C895,620 840,670 775,690 L745,700 C740,800 742,950 745,1048 L662,1048 C658,950 668,780 680,665 C650,620 640,580 640,520 Z"/>

    <g class="settings-badge">
      <circle cx="705" cy="352" r="33" fill="var(--paper)" stroke="#222" stroke-width="1"/>
      <text class="badge-text"><textPath href="#badge-arc" textLength="192" lengthAdjust="spacingAndGlyphs">FÜNF VERSCHIEDENE EINSTELLUNGEN</textPath></text>
      <circle cx="705" cy="352" r="20" fill="var(--mist)" role="img" aria-label="Symbol Wasserstrahl"/>
    </g>

    <text class="headline" transform="translate(965,1020) rotate(-90)" font-size="98" textLength="705" lengthAdjust="spacingAndGlyphs">DUSCHKOPF</text>
    <text class="headline" transform="translate(872,1020) rotate(-90)" font-size="56" textLength="320" lengthAdjust="spacingAndGlyphs">MASSAGE</text>
    <text class="headline" transform="translate(820,1020) rotate(-90)" font-size="56" textLength="140" lengthAdjust="spacingAndGlyphs">5IN1</text>

    <text class="claim" transform="translate(1070,824) rotate(-90)" textLength="318" lengthAdjust="spacingAndGlyphs">DEIN URLAUB FÜR ZUHAUSE.</text>
  </g>

  <!-- Hang tab slots -->
  <g class="hang-slots">
    <path class="cut" d="M250,143 H317 A9,9 0 0 1 317,160 H296 A12,12 0 0 1 272,160 H250 A9,9 0 0 1 250,143 Z"/>
    <path class="cut" d="M250,234 H317 A9,9 0 0 0 317,217 H296 A12,12 0 0 0 272,217 H250 A9,9 0 0 0 250,234 Z"/>
  </g>

  <!-- Cut and fold lines -->
  <g class="cut-lines">
    <path class="cut" d="M106,270 V68 L112,62 H456 L462,68 V270"/>
    <line class="cut" x1="106" y1="105" x2="462" y2="105"/>
    <line class="cut" x1="106" y1="188" x2="462" y2="188"/>
    <path class="cut" d="M106,270 L61,282 V1044 L106,1056"/>
    <rect class="cut" x="106" y="270" width="356" height="786"/>
    <path class="cut" d="M106,1056 L195,1140 V1183 H372 V1140 L462,1056"/>

    <path class="cut" d="M462,270 L478,160 H608 L614,242 L625,252"/>
    <rect class="cut" x="462" y="270" width="163" height="786"/>
    <path class="cut" d="M462,1056 V1183 H543 V1140 L625,1056"/>

    <path class="cut" d="M625,270 V68 L631,62 H976 L982,68 V270"/>
    <line class="cut" x1="625" y1="105" x2="982" y2="105"/>
    <rect class="cut" x="625" y="270" width="357" height="786"/>
    <path class="cut" d="M625,1056 V1183 H715 V1140 H892 V1183 H982 V1056"/>

    <path class="cut" d="M982,252 L993,242 L999,160 H1128 L1145,270"/>
    <rect class="cut" x="982" y="270" width="163" height="786"/>
    <path class="cut" d="M982,1056 L1064,1140 V1183 H1145 V1056"/>
  </g>
</svg>
</body>
</html>
```